Stationary Design
Wexley Money Services
To all designer:
Thanks for submitting the revision and they are looking great. Here are some small minor adjustment on my information:
1) Envelope: Just need my mailing address
2) Folder: Just need my mailing address and Web address
3) Letterhead: Just need my phone number, mailing address and web address.
I made a mistake previously on my logo design project not finalizing the details and end up wasting a lot of time.
I appreciate everyone's patient on this.
To all designer: Just a friendly reminder:
Business Card: Please remove my license number.
Lettheads: No need to include my email and cell number.
Envelope: Just need to include website address and mailing address.
Thanks!!
pelicanjot (#29)
Really nice business card. Is the watermark suppose to cover front and back? It is possible you can make it all fit on the front side? Can you shrink the font size for my name and title as well as the logo on the backside of card?
qirrr (#25,#26)
Thanks for designing the whole set as well. This is a very creative design and I've been starting at it for at least 20 minutes trying to visualize printing this on a regular folder/card/letterhead..etc. I think the wave/green shape might need to be shrink down on the folders and business card. It maybe a bit overpowering.
Velustro (#18, #19)
Thank you for designing the whole set. I really appreciated. For the business card, if you can shrink the watermark logo on the back side, would look really nice. For the folder, I would prefer to see less of the green and black color. The folder would actually work for me if you even make the front shape smaller and backside white color with watermark of the logo.
Plenmorix (#17)
Thanks for providing few variations for the design.
I like the second letterhead but maybe we can look at using the watermark in the middle instead of the logo on the bottom. For the business card, the last one is nice. I would prefer to see them smaller size (logo and fonts) and possibly use watermark for the shape instead of solid green.
Tarn47 (#6, #22)
I like the layout of #6. If possible, we can look at grey/white background on the backside and maybe shrinking the logo down a bit on the front side. #22's business card is nice as well. I think grey/white backside will look really nice. I liked the placement of information for the envelope and letterhead. The watermark is a nice touch. Is it possible to look at possibly reducing the logo down a bit? I'm curious to see what it looks like.
owlcrafts (#2)
I liked the business card a lot, especially the backside. For the letterhead, as per my comment to everyone, maybe shrinking my contact information down more. Not sure if you can incorporate some grey watermark of the logo into the letterhead.
Envelope i really liked as well. Especially the backside. For the front, is it possible to shrink the logo down a bit and lower it? I won't be using the window envelope.
For the folder, I think it has too much of either green or grey. Is it possible to utilize less color and more watermark/white background?
Hi all, thanks for the additional submission and revision. I really do appreciated. I've decided to eliminate a few designs and keep the best ones from each of designer. This will clear up some space.
To all Designers:
Business card: Please remove license number and less green in general.
Letterhead: Pleas remove my email and i would like the contact information as less visible as possible. So maybe try smaller size font or placing it on bottom or side of the sheet.
Folders: Doesn't have to be too much color usage. It can be simple.
Envelope: Can be simple as well. I actually liked most of designers' envelope. Each has it's own unique style.
Updated. Thanks!
For letterheads and envelope. You don't have to include all the information. Just need:
1) address
2) phone, fax and toll free (do not need my cell)
You don't have to include my Lic#/cell phone.
Thanks.
Thanks for the prompt submission everyone. I just designed this logo last week and the color green is fairly new to me. I think if possible, to use less Green and more of the grey and white. That may help to bring up the green more. For example, like #2 and #5. Really nice usage of the grey on the back of the card.
For the layout of the content (biz card), i like the information placement on #2, #4, #6 and #16. The information are aligned and my name is clearly recognize without overpowering the rest of the information.

```html
<!DOCTYPE html>
<html lang="en">
<head>
<meta charset="utf-8">
<title>Wexley Money Services – Stationery</title>
<link href="https://fonts.googleapis.com/css2?family=Questrial&display=swap" rel="stylesheet">
<style>
  :root {
    --stage: #8a8e90;
    --paper: #ffffff;
    --green: #7cb342;
    --green-soft: #a9cf7c;
    --ink: #555a5e;
    --ink-light: #8b8f92;
    --grey-card: #8d8f91;
    --grey-card-dark: #6f7173;
    --watermark: rgba(120, 140, 100, 0.10);
    --font: "Questrial", sans-serif;
  }
  * { box-sizing: border-box; margin: 0; padding: 0; }
  html, body { width: 1200px; height: 734px; overflow: hidden; }
  body { background: var(--stage); font-family: var(--font); color: var(--ink); position: relative; }

  .piece { position: absolute; background: var(--paper); box-shadow: 0 4px 14px rgba(0,0,0,.28); overflow: hidden; }

  /* brand lockup */
  .brand { display: flex; align-items: center; gap: 8px; }
  .brand-dot { border-radius: 50%; background: var(--green); flex: none; }
  .brand-name { color: var(--ink); font-weight: 400; white-space: nowrap; letter-spacing: .2px; }

  .watermark-circle { position: absolute; border-radius: 50%; background: var(--watermark); }

  /* business card front */
  .card-front { left: 360px; top: 36px; width: 300px; height: 168px; border-radius: 8px; }
  .card-front .brand { position: absolute; left: 14px; top: 26px; width: 124px; flex-direction: column; gap: 5px; }
  .card-front .brand-dot { width: 20px; height: 20px; }
  .card-front .brand-name { font-size: 10.5px; }
  .card-front .divider { position: absolute; left: 150px; top: 20px; width: 1px; height: 128px; background: var(--green-soft); }
  .card-front .holder { position: absolute; left: 162px; top: 20px; }
  .holder-name { color: var(--green); font-size: 14px; }
  .holder-title { font-size: 7.5px; color: var(--ink-light); margin-top: 2px; }
  .card-front .contact { position: absolute; left: 162px; top: 62px; font-size: 6.5px; line-height: 1.55; color: var(--ink-light); }
  .contact .gap { height: 6px; }

  /* business card back */
  .card-back { left: 312px; top: 222px; width: 236px; height: 149px; border-radius: 8px;
    background: linear-gradient(135deg, var(--grey-card) 0%, var(--grey-card-dark) 100%); }
  .card-back .watermark-circle { left: 20px; top: -20px; width: 150px; height: 150px; background: rgba(255,255,255,.08); }
  .card-back .brand { position: absolute; right: 18px; top: 62px; }
  .card-back .brand-dot { width: 14px; height: 14px; background: #fff; }
  .card-back .brand-name { color: #fff; font-size: 8px; }
  .card-back .web { position: absolute; right: 18px; bottom: 14px; color: #e6e6e6; font-size: 6px; }

  /* envelope back */
  .envelope-back { left: 223px; top: 392px; width: 461px; height: 126px; }
  .envelope-back svg { position: absolute; inset: 0; }
  .envelope-back .brand-dot { position: absolute; left: 220px; top: 20px; width: 20px; height: 20px; background: #fff; }

  /* envelope front */
  .envelope-front { left: 223px; top: 532px; width: 461px; height: 178px; }
  .envelope-front .watermark-circle { left: 300px; top: 18px; width: 140px; height: 140px; }
  .envelope-front .brand { position: absolute; left: 20px; top: 26px; }
  .envelope-front .brand-dot { width: 22px; height: 22px; }
  .envelope-front .brand-name { font-size: 13px; }
  .envelope-front .return { position: absolute; left: 20px; top: 60px; font-size: 6.5px; line-height: 1.6; color: var(--ink-light); }

  /* letterhead */
  .letterhead { left: 703px; top: 36px; width: 406px; height: 664px; }
  .letterhead .brand { position: absolute; left: 26px; top: 26px; }
  .letterhead .brand-dot { width: 24px; height: 24px; }
  .letterhead .brand-name { font-size: 14px; }
  .letterhead .watermark-circle { left: 110px; top: 300px; width: 200px; height: 200px; }
  .letterhead .footer-rule { position: absolute; left: 190px; right: 26px; bottom: 48px; height: 1px; background: var(--green-soft); }
  .letterhead .footer { position: absolute; right: 26px; bottom: 22px; text-align: right; font-size: 6px; line-height: 1.6; color: var(--ink-light); }
</style>
</head>
<body>

  <section class="piece card-front">
    <div class="brand"><span class="brand-dot"></span><span class="brand-name">Wexley Money Services</span></div>
    <div class="divider"></div>
    <div class="holder">
      <div class="holder-name">Mara Ellison</div>
      <div class="holder-title">Managing Partner</div>
    </div>
    <div class="contact">
      <div>2410 Harbor View Road, Suite 120</div>
      <div>Lakeside, CA 94100</div>
      <div class="gap"></div>
      <div>Tel: 555.201.4400</div>
      <div>Fax: 555.201.4401</div>
      <div>Toll Free: 800.555.0190</div>
      <div class="gap"></div>
      <div>mara@wexleymoney.example</div>
    </div>
  </section>

  <section class="piece card-back">
    <span class="watermark-circle"></span>
    <div class="brand"><span class="brand-dot"></span><span class="brand-name">Wexley Money Services</span></div>
    <div class="web">www.wexleymoney.example</div>
  </section>

  <section class="piece envelope-back">
    <svg width="461" height="126" viewBox="0 0 461 126">
      <defs>
        <linearGradient id="flapShade" x1="0" y1="0" x2="0" y2="1">
          <stop offset="0" stop-color="#8d8f91"/>
          <stop offset="1" stop-color="#6c6e70"/>
        </linearGradient>
      </defs>
      <polygon points="0,0 461,0 461,12 250,80 211,80 0,12" fill="url(#flapShade)"/>
      <line x1="0" y1="125" x2="461" y2="125" stroke="#e4e4e2"/>
    </svg>
    <span class="brand-dot"></span>
  </section>

  <section class="piece envelope-front">
    <span class="watermark-circle"></span>
    <div class="brand"><span class="brand-dot"></span><span class="brand-name">Wexley Money Services</span></div>
    <div class="return">
      <div>2410 Harbor View Road, Suite 120, Lakeside, CA 94100</div>
      <div>Tel 555.201.4400 &nbsp;Fax 555.201.4401 &nbsp;Web wexleymoney.example</div>
    </div>
  </section>

  <section class="piece letterhead">
    <div class="brand"><span class="brand-dot"></span><span class="brand-name">Wexley Money Services</span></div>
    <span class="watermark-circle"></span>
    <div class="footer-rule"></div>
    <div class="footer">
      <div>2410 Harbor View Road, Suite 120, Lakeside, CA 94100</div>
      <div>Tel 555.201.4400 &nbsp;Fax 555.201.4401 &nbsp;Toll Free 800.555.0190</div>
    </div>
  </section>

</body>
</html>
```